Email Signatures

I would like to create a new email signature for my team. The design will be the same for everyone, with only individual details such as name and email changing. You can also see our brand style on our website. https://www.tlmbespokehomes.com.au/

Target Market(s)

Clients for new builds or renovations

Industry/Entity Type

Construction

Colors

Designer to choose colors to be used in the design.

```html
<!DOCTYPE html>
<html lang="en">
<head>
<meta charset="utf-8">
<title>Email Signature – TLM Bespoke Homes</title>
<link rel="stylesheet" href="https://fonts.googleapis.com/css2?family=Barlow:ital,wght@1,800&family=Poppins:wght@400;500;600&display=swap">
<style>
  :root {
    --page-bg: #bcbcbc;
    --card-bg: #ffffff;
    --brand-green: #0e9a43;
    --ink: #2b2b2b;
    --divider: #4a4a4a;
  }
  html, body {
    margin: 0;
    width: 1200px;
    height: 1200px;
    overflow: hidden;
    background: var(--page-bg);
    font-family: "Poppins", sans-serif;
  }
  .signature {
    position: absolute;
    left: 300px;
    top: 515px;
    width: 600px;
    height: 170px;
    background: var(--card-bg);
  }
  .brand {
    position: absolute;
    left: 50px;
    top: 55px;
    width: 125px;
    height: 60px;
    display: flex;
    align-items: center;
    justify-content: center;
    gap: 8px;
  }
  .brand-square {
    width: 14px;
    height: 14px;
    background: var(--brand-green);
  }
  .brand-name {
    font-family: "Poppins", sans-serif;
    font-weight: 600;
    font-size: 40px;
    line-height: 1;
    color: var(--ink);
    letter-spacing: 1px;
  }
  .divider {
    position: absolute;
    left: 205px;
    top: 20px;
    width: 1px;
    height: 130px;
    background: var(--divider);
  }
  .person-name {
    position: absolute;
    left: 235px;
    top: 22px;
    margin: 0;
    font-family: "Barlow", sans-serif;
    font-style: italic;
    font-weight: 800;
    font-size: 28px;
    line-height: 1;
    color: var(--brand-green);
    letter-spacing: 0.5px;
  }
  .person-role {
    position: absolute;
    left: 235px;
    top: 50px;
    margin: 0;
    font-weight: 500;
    font-size: 17px;
    line-height: 1.2;
    color: var(--ink);
  }
  .social {
    position: absolute;
    right: 35px;
    top: 27px;
    display: flex;
    gap: 7px;
  }
  .social-tile {
    width: 27px;
    height: 27px;
    border-radius: 6px;
    background: var(--brand-green);
  }
  .contact {
    position: absolute;
    left: 235px;
    top: 86px;
    font-size: 11.5px;
    color: var(--ink);
  }
  .contact-row {
    display: flex;
    align-items: center;
    height: 19.5px;
  }
  .contact-item {
    display: flex;
    align-items: center;
    gap: 4px;
    margin-right: 15px;
  }
  .contact-item svg {
    width: 13px;
    height: 13px;
    fill: var(--brand-green);
    flex: none;
  }
</style>
</head>
<body>
  <section class="signature">
    <div class="brand">
      <span class="brand-square"></span>
      <span class="brand-name">TLM</span>
    </div>

    <div class="divider"></div>

    <h1 class="person-name">LIAM HARTLEY</h1>
    <p class="person-role">General Manager</p>

    <div class="social">
      <span class="social-tile" aria-label="Social profile"></span>
      <span class="social-tile" aria-label="Social profile"></span>
    </div>

    <div class="contact">
      <div class="contact-row">
        <span class="contact-item">
          <svg viewBox="0 0 24 24" aria-hidden="true"><path d="M6.6 10.8a15.1 15.1 0 0 0 6.6 6.6l2.2-2.2a1 1 0 0 1 1-.25 11.4 11.4 0 0 0 3.6.57 1 1 0 0 1 1 1V20a1 1 0 0 1-1 1A17 17 0 0 1 3 4a1 1 0 0 1 1-1h3.5a1 1 0 0 1 1 1c0 1.25.2 2.45.57 3.57a1 1 0 0 1-.25 1z"/></svg>
          0400 123 456
        </span>
        <span class="contact-item">
          <svg viewBox="0 0 24 24" aria-hidden="true"><path d="M2 5h20v14H2z M4 7v.4l8 5.3 8-5.3V7z" fill-rule="evenodd"/></svg>
          info@tlmbespokehomes.com.au
        </span>
      </div>
      <div class="contact-row">
        <span class="contact-item">
          <svg viewBox="0 0 24 24" aria-hidden="true"><path d="M12 2a7 7 0 0 0-7 7c0 5.2 7 13 7 13s7-7.8 7-13a7 7 0 0 0-7-7zm0 9.5A2.5 2.5 0 1 1 12 6.5a2.5 2.5 0 0 1 0 5z"/></svg>
          Kingsbay, Northvale, Eastland
        </span>
      </div>
      <div class="contact-row">
        <span class="contact-item">
          <svg viewBox="0 0 24 24" aria-hidden="true"><path d="M12 2a10 10 0 1 0 0 20 10 10 0 0 0 0-20zm6.9 6h-3a15.6 15.6 0 0 0-1.4-3.6A8 8 0 0 1 18.9 8zM12 4c.8 1.2 1.5 2.5 1.9 4h-3.8c.4-1.5 1.1-2.8 1.9-4zM4.3 14a8.2 8.2 0 0 1 0-4h3.4a16.5 16.5 0 0 0 0 4zm.8 2h3a15.6 15.6 0 0 0 1.4 3.6A8 8 0 0 1 5.1 16zm3-8h-3a8 8 0 0 1 4.4-3.6A15.6 15.6 0 0 0 8.1 8zM12 20c-.8-1.2-1.5-2.5-1.9-4h3.8c-.4 1.5-1.1 2.8-1.9 4zm2.3-6H9.7a14.7 14.7 0 0 1 0-4h4.6a14.7 14.7 0 0 1 0 4zm.3 5.6A15.6 15.6 0 0 0 16 16h3a8 8 0 0 1-4.4 3.6zm1.7-5.6a16.5 16.5 0 0 0 0-4h3.4a8.2 8.2 0 0 1 0 4z"/></svg>
          www.tlmbespokehomes.com.au
        </span>
      </div>
    </div>
  </section>
</body>
</html>
```